Business Card Design for Photographer

Updating business card design. Must use included logo. We're a luxury wedding photography business. Elegancy, luxury, consistency are messages we wish to convey.

Visit our website at www.colbyvarnway.com to familiarize yourself more with our brand design currently (fonts, colors etc.). This is what we want to maintain.

Target Market(s)

Luxury Brides and Grooms

Industry/Entity Type

Wedding

Contact Information for Business Card

Current logo (attached to brief)
Name: Colby Varnway
Phone: 5208813047
website/blog
Email

Requirements
Must have
• Current logo (attached to brief)
• Name: Colby Varnway
• Phone: 5208813047
• website/blog
• Email
• Instagram username
Should not have
• bright colors, fonts that don't suit our brand (visit www.colbyvarnway.com)

```html
<!DOCTYPE html>
<html lang="en">
<head>
<meta charset="utf-8">
<title>Colby Varnway Photographers – Business Card</title>
<link rel="stylesheet" href="https://fonts.googleapis.com/css2?family=Marcellus+SC&family=Crimson+Text&display=swap">
<style>
  :root {
    --page-bg: #ececec;
    --card-bg: #fbfbf9;
    --brand: #5e6966;
    --ink: #2f3332;
    --icon: #7c8583;
    --photo-dark: #5d5650;
    --photo-mid: #8a817a;
    --photo-bloom: #e7a79b;
    --photo-light: #d9dcd2;
  }
  * { box-sizing: border-box; margin: 0; padding: 0; }
  html, body { width: 858px; height: 1200px; overflow: hidden; }
  body { background: var(--page-bg); position: relative; font-family: "Crimson Text", Georgia, serif; }

  .card {
    position: absolute;
    left: 149px;
    width: 560px;
    height: 326px;
    background: var(--card-bg);
    overflow: hidden;
  }
  .card--front { top: 150px; }
  .card--back { top: 640px; }

  /* Front */
  .front-mark {
    position: absolute;
    left: 243px; top: 66px;
    width: 74px; height: 74px;
    background: var(--brand);
  }
  .front-name {
    position: absolute;
    left: 0; right: 0; top: 166px;
    text-align: center;
    font-family: "Marcellus SC", Georgia, serif;
    font-size: 33px;
    letter-spacing: 4px;
    color: var(--brand);
  }
  .front-tagline {
    position: absolute;
    left: 0; right: 0; top: 226px;
    text-align: center;
    font-family: "Marcellus SC", Georgia, serif;
    font-size: 16px;
    letter-spacing: 7px;
    color: var(--brand);
  }

  /* Back */
  .bouquet-photo {
    position: absolute;
    left: 0; top: 0;
    width: 240px; height: 100%;
    background:
      radial-gradient(ellipse 55% 35% at 50% 40%, var(--photo-bloom) 0%, rgba(231,167,155,0.6) 40%, rgba(217,220,210,0.3) 70%, transparent 100%),
      linear-gradient(180deg, var(--photo-dark) 0%, var(--photo-mid) 55%, #6e6862 100%);
  }
  .back-brand {
    position: absolute;
    right: 40px; top: 56px;
    display: flex;
    align-items: center;
    gap: 6px;
  }
  .back-brand__text {
    text-align: right;
    font-family: "Marcellus SC", Georgia, serif;
    color: var(--brand);
    line-height: 1;
  }
  .back-brand__name { font-size: 19px; letter-spacing: 2px; }
  .back-brand__tagline { font-size: 9px; letter-spacing: 3.4px; margin-top: 3px; }
  .back-brand__mark { width: 46px; height: 46px; background: var(--brand); }

  .contact {
    position: absolute;
    left: 266px; top: 145px;
    list-style: none;
    color: var(--ink);
    font-size: 20px;
    line-height: 28px;
  }
  .contact__item { display: flex; align-items: center; gap: 8px; }
  .contact__item--name { padding-left: 26px; }
  .contact__icon { width: 18px; height: 18px; flex: none; }
</style>
</head>
<body>

<section class="card card--front" aria-label="Business card front">
  <div class="front-mark"></div>
  <div class="front-name">Colby Varnway</div>
  <div class="front-tagline">Photographers</div>
</section>

<section class="card card--back" aria-label="Business card back">
  <div class="bouquet-photo" role="img" aria-label="Photograph of a pastel wedding bouquet of pink roses against weathered wood"></div>

  <div class="back-brand">
    <div class="back-brand__text">
      <div class="back-brand__name">Colby Varnway</div>
      <div class="back-brand__tagline">Photographers</div>
    </div>
    <div class="back-brand__mark"></div>
  </div>

  <ul class="contact">
    <li class="contact__item contact__item--name">Colby Varnway</li>
    <li class="contact__item">
      <svg class="contact__icon" viewBox="0 0 18 18" fill="none" stroke="var(--icon)" stroke-width="1.4"><rect x="5" y="2" width="8" height="14" rx="1.5"/><line x1="8" y1="13.5" x2="10" y2="13.5"/></svg>
      (520) 881-3047
    </li>
    <li class="contact__item">
      <svg class="contact__icon" viewBox="0 0 18 18" fill="none" stroke="var(--icon)" stroke-width="1.3"><circle cx="9" cy="9" r="7"/><ellipse cx="9" cy="9" rx="3" ry="7"/><line x1="2" y1="9" x2="16" y2="9"/></svg>
      www.colbyvarnway.com
    </li>
    <li class="contact__item">
      <svg class="contact__icon" viewBox="0 0 18 18" fill="none" stroke="var(--icon)" stroke-width="1.3"><rect x="2" y="4" width="14" height="10"/><polyline points="2,4 9,10 16,4"/></svg>
      colby@colbyvarnway.com
    </li>
    <li class="contact__item">
      <svg class="contact__icon" viewBox="0 0 18 18" fill="none" stroke="var(--icon)" stroke-width="1.4"><rect x="3" y="3" width="12" height="12"/></svg>
      @colbyvarnwayphoto
    </li>
  </ul>
</section>

</body>
</html>
```